Bakery Replacement Lighted Sign Face

We are opening a new bakery that sells only cakes. The name is "The Willow Lantern." We are replacing the current sign face with a new look that states our name and makes a bold statement of fun. We will be known for having 101 cakes that are always ready for immediate pickup or delivery. Our colors are pink, orange, and lime green. An image is provided to see the colors.

Target Market(s)

people who buy cakes for parties and all other occasions

Industry/Entity Type

Cakes

Other font styles liked:
• look at the logo and file for the main font name

Colors
59FF00
82FF00
B8FF75
E3FFCB
F4FFEA
F0912C
F2A743
F7CA91
FBE8D2
FDF5EE
EB3D1F
EC4F4E
F09395
F8D3D4
FCEDEE

Requirements
Must have
• The name of the bakery. Logo can be used as is or changed as shown in one of the uploaded PDFs. Must use either pink, orange, lime green, white, or black. We prefer a bright pink background with white lettering as our first choice, but are willing to be open minded to see all creative concepts. Also the sign is 14 feet long and 42 inches tall so the artwork must fit within those boundaries. Also keep in mind the sign does have a 4 inch black frame. So the graphics area is actually 13 feet 2 inches by 3 feet. Also, in the attached pdf that shows a rough possible layout, the words "101 cakes to go" is on the sign. It is NOT a must. Only use the wording if it adds to your design.
Nice to have
• You are welcome to add additional stars or other fun graphics that could look good.
Should not have
• No images of cakes or other bakery products.

```html
<!DOCTYPE html>
<html lang="en">
<head>
<meta charset="utf-8">
<title>The Willow Lantern – Sign Face</title>
<link rel="stylesheet" href="https://fonts.googleapis.com/css2?family=Fredoka:wght@600;700&display=swap">
<style>
  :root {
    --sign-pink: #d9447f;
    --sign-pink-soft: #e06a98;
    --icing-white: #ffffff;
    --shadow-black: #000000;
  }
  * { margin: 0; padding: 0; box-sizing: border-box; }
  html, body {
    width: 1200px;
    height: 273px;
    overflow: hidden;
    background: var(--sign-pink);
  }
  .sign-face {
    position: relative;
    width: 1200px;
    height: 273px;
    background: var(--sign-pink);
    overflow: hidden;
    font-family: "Fredoka", sans-serif;
  }
  .icing-drip {
    position: absolute;
    top: 0;
    left: 219px;
    width: 764px;
    height: 38px;
    background: linear-gradient(to bottom, var(--icing-white) 0%, rgba(255,255,255,0.85) 55%, rgba(255,255,255,0) 100%);
  }
  .doodle-border {
    position: absolute;
    top: 0;
    width: 110px;
    height: 273px;
    background: linear-gradient(to bottom, var(--sign-pink-soft), var(--sign-pink) 50%, var(--sign-pink-soft));
  }
  .doodle-border--left { left: 0; }
  .doodle-border--right { right: 0; }
  .sparkles {
    position: absolute;
    inset: 0;
  }
  .brand-name {
    position: absolute;
    top: 84px;
    left: 0;
    width: 1200px;
    text-align: center;
    font-weight: 600;
    font-size: 34px;
    line-height: 1;
    color: var(--icing-white);
  }
  .tagline {
    position: absolute;
    top: 168px;
    left: 0;
    width: 1200px;
    text-align: center;
    font-weight: 700;
    font-size: 64px;
    line-height: 1;
    color: var(--icing-white);
    letter-spacing: 1px;
    text-shadow: 3px 4px 3px var(--shadow-black);
  }
</style>
</head>
<body>
  <main class="sign-face">
    <div class="icing-drip" role="img" aria-label="White icing dripping along the top edge"></div>
    <div class="doodle-border doodle-border--left" role="img" aria-label="White line doodles of cupcakes, strawberries and hearts"></div>
    <div class="doodle-border doodle-border--right" role="img" aria-label="White line doodles of cupcakes, strawberries and hearts"></div>

    <svg class="sparkles" width="1200" height="273" viewBox="0 0 1200 273" aria-hidden="true">
      <g fill="#ffffff">
        <!-- left group -->
        <polygon points="258,91 269,109 289,104 284,124 302,135 284,146 289,166 269,161 258,179 247,161 227,166 232,146 214,135 232,124 227,104 247,109"/>
        <polygon points="142,121 149,141 168,134 157,151 168,168 149,161 142,181 135,161 116,168 127,151 116,134 135,141"/>
        <circle cx="143" cy="75" r="3.5"/>
        <circle cx="186" cy="92" r="3.5"/>
        <!-- right group -->
        <polygon points="955,91 966,109 986,104 981,124 999,135 981,146 986,166 966,161 955,179 944,161 924,166 929,146 911,135 929,124 924,104 944,109"/>
        <polygon points="1071,121 1078,141 1097,134 1086,151 1097,168 1078,161 1071,181 1064,161 1045,168 1056,151 1045,134 1064,141"/>
        <circle cx="1069" cy="75" r="3.5"/>
        <circle cx="1026" cy="92" r="3.5"/>
      </g>
    </svg>

    <h1 class="brand-name">The Willow Lantern</h1>
    <p class="tagline">101 cakes to go</p>
  </main>
</body>
</html>
```